KLVN- company with a mission

KLVN LLC stands for keeping lanterns vividly nigh (non profit arm is called lantern kept foundation)—our business is based out of New York City and has a non-profit arm where for every bar you purchase, we donate a bar (don’t want any designs that limits us to only soap). Currently working with South Africa. We want the focus to be organic/natural soap with a mission.
What our website needs to…achieve:
Purpose = branding, building up interesting leaving up to launch date, then a full functional site for selling soap (for now) with a mission. With that said, there will need to be a page designed for “COMING SOON” – with a place to post our teaser 30 second video (kind of like a commercial/movie trailer) – until everything else is done.
We are the first in the industry to do one for one (or …50/50). Most companies that do charity work are mostly for every $$$ we donate $0.10, or 1% of XXX. We are starting out to run the non-profit arm as well not just after we reach certain milestones. In addition, we will be transparent for the non-profit side whereas most of the time when you donate, you have no idea where the money ends up going.
IN ADDITION: we still need to be clean/elegant – and selling our soap; so website will need to 1. Showcase our products, 2. Be very clear that we have a mission (not sure if there is a way to show case both our soap AND our mission)
Some sites we like:
Pelarin.com—like them in terms of business model—in terms of their website: like how their site is clean and friendly, but it seems too cluttered
www.quendaltrove.com -- similar business model, www.fevriskel.com, brimavault.com, marshlintsoap.com
Tivel.com: like this a lot better than gavroue.com, however, major dislike of the typeface. Okay about the neutral colors…although feel like we need something a bit more cheerful here and there for our mission
Zkindle.net, brimavault.com, fennawick.com: like how they are clean and showcase well
**** However, our site also needs to convey messages like: www.wellspringpledge.org, www.rinsewidely.org
Looking for a clean, simple design. Modern, clutter-free, and inviting. Definitely do not want an arts and crafty/flowery feel. We do need something…cheerful for our nonprofit purposes.
Examples of sites we don’t like: quillmarbet.com, corvelpatchsoap.com
7 pages/ tabs maybe? (About us…video page (to show case what we are doing –currently my partner is in South Africa filming what our mission will be able to do – give children and those in need soap), FAQs, soap products, terms & conditions, contact us page, blog page……nothing too crazy).
For now, for designing purposes, please use any example texts whether it’s the about us page, mission page..policies.. and for the soap/products pages—please use example you can find online – it is fine, we just need the design done for now.
I have also attached our logo file. Please let me know if you have any questions! Thanks!
Something to consider....
pelarin.com and quendaltrove.com are probably our largest competitor out of all the websites I mentioned as they have a very similar business model where it is is a company with a mission. Homepage makes that clear that for every pair of shoes/ glasses you purchase, they give a pair. Another thing to note...is that they have been in business for a few years so their website probably have changed to more commercial than focusing/marketing on the mission of doing good. While we don't want that to be the total focus, we do need it to be present on the homepage/front page.

```html
<!DOCTYPE html>
<html lang="en">
<head>
<meta charset="utf-8">
<title>KLVN – Soap with a mission</title>
<link rel="stylesheet" href="https://fonts.googleapis.com/css2?family=Bebas+Neue&family=Open+Sans:wght@400;600;700&display=swap">
<style>
:root{
  --ink:#222;
  --topbar:#1f1f1f;
  --cream:#fdf0dc;
  --sand:#ede1cc;
  --cocoa:#2e2a23;
  --orange:#f6a65a;
  --orange-deep:#ee9a4a;
  --slate:#3a3a3a;
  --footer:#333333;
  --footer-line:#444;
  --paper:#ffffff;
  --muted:#cfc8bc;
  --link-blue:#3b5998;
}
*{box-sizing:border-box;margin:0;padding:0}
html,body{width:775px;height:1200px;overflow:hidden}
body{font-family:"Open Sans",Arial,sans-serif;color:var(--ink);background:var(--paper);position:relative}
.abs{position:absolute}
.topbar{left:0;top:0;width:775px;height:19px;background:var(--topbar);color:#eee;font-size:7.5px;line-height:19px}
.topbar .left{left:104px}
.topbar .right{right:128px}
.topbar span{margin-right:8px}
.header{left:0;top:19px;width:775px;height:51px;background:var(--cream)}
.brand{left:104px;top:4px;display:flex;align-items:center;gap:5px}
.brand-dot{width:42px;height:42px;border-radius:50%;background:var(--orange);display:flex;align-items:center;justify-content:center;color:#fff;font-weight:700;font-size:11px}
.nav{left:243px;top:18px;font-size:8.5px;color:#444;letter-spacing:.2px}
.nav span{position:absolute;white-space:nowrap}
.nav-dot{width:6px;height:6px;border-radius:50%;background:var(--orange);left:257px;top:50px}
.hero{left:0;top:70px;width:775px;height:282px;background:linear-gradient(135deg,#5a6b86 0%,#b98a6c 35%,#c98f70 60%,#7a4a35 100%)}
.hero-text{left:0;top:60px;width:775px;text-align:center;font-family:"Bebas Neue",Impact,sans-serif;color:#fff;font-size:27px;line-height:34px;letter-spacing:.3px}
.hero-dots{top:330px;left:618px;display:flex;gap:7px}
.hero-dots i{display:block;width:10px;height:10px;background:#3a2a1a}
.hero-dots i:first-child{background:var(--orange)}
.approach{left:0;top:352px;width:775px;height:238px;background:var(--cocoa);color:#fff}
.tag{background:var(--orange);color:#fff;font-size:8px;font-weight:700;letter-spacing:.4px;border-radius:3px;text-align:center;line-height:22px;height:22px}
.intro{font-size:6.5px;line-height:8px;color:#eee}
.video{left:103px;top:66px;width:252px;height:151px;background:linear-gradient(160deg,#b7a983,#d6c9a6 60%,#bfb08a);border-radius:4px;overflow:hidden}
.video-title{left:8px;top:8px;display:flex;align-items:center;gap:8px;color:#fff;font-size:8.5px;font-weight:600}
.video-title b{width:31px;height:25px;background:#fff;border-radius:2px;display:flex;align-items:center;justify-content:center}
.video-title b i{width:19px;height:19px;border-radius:50%;background:var(--orange)}
.video-icons{right:8px;top:18px;display:flex;flex-direction:column;gap:4px}
.video-icons div{width:18px;height:17px;background:#3d3a33;border-radius:2px;display:flex;align-items:center;justify-content:center}
.video-bar{left:0;bottom:0;width:252px;height:20px;background:#3c3c3c;color:#ccc;font-size:6.5px;line-height:20px}
.label{font-size:7px;font-weight:700;letter-spacing:.4px;line-height:14px;color:#f2ece2}
.photo{border-radius:4px}
.latest{left:0;top:590px;width:775px;height:170px;background:var(--sand)}
.arrow{font-size:18px;color:#333;top:80px}
.mission{left:0;top:760px;width:775px;height:204px;background:var(--cream)}
.body-copy{font-size:7px;line-height:10.3px;color:#333}
.btn-dark{background:#2d2d2d;color:#fff;font-size:7px;line-height:14px;padding:0 6px;border-radius:1px}
.offer{left:302px;top:18px;width:136px;height:77px;background:var(--orange);color:#fff;padding:30px 10px 0;border-radius:2px}
.offer h3{font-size:10.5px;font-weight:700;letter-spacing:.4px}
.offer p{font-size:7.5px}
.ship{left:303px;top:108px;width:135px;height:72px;background:var(--slate);color:#fff;padding:14px 14px 0 21px;border-radius:2px}
.ship h3{font-size:8px;font-weight:700;letter-spacing:.4px;margin-bottom:6px}
.ship p{font-size:7px;line-height:10px}
.social-box{left:468px;top:18px;width:194px;height:168px;background:var(--paper);border-radius:3px;padding:20px 18px}
.social-box h3{font-size:11px;font-weight:700;letter-spacing:.3px;color:#222}
.page-row{display:flex;gap:5px;margin-top:5px;align-items:flex-start}
.page-row .dot{width:20px;height:20px;border-radius:50%;background:var(--orange)}
.page-name{color:var(--link-blue);font-weight:700;font-size:8px}
.like{display:inline-block;background:var(--link-blue);color:#fff;font-size:6.5px;padding:0 4px;line-height:10px;border-radius:2px}
.small{font-size:7px;color:#333}
.footer{left:0;top:964px;width:775px;height:200px;background:var(--footer);color:#fff}
.footer h4{font-weight:400;font-size:11px;letter-spacing:.3px;position:absolute;top:16px}
.links{position:absolute;top:48px;font-size:7px;color:#e6e6e6;line-height:17.2px}
.vline{position:absolute;top:48px;width:1px;height:120px;background:var(--footer-line)}
.soc{position:absolute;left:426px;width:17px;height:17px;border-radius:50%;background:#fff}
.store{position:absolute;left:528px;top:48px;font-size:7px;line-height:17.2px;color:#e6e6e6}
.store b{font-size:9.5px;font-weight:400;margin-right:4px}
.copyright{left:0;top:1164px;width:775px;height:36px;background:#f5f5f5;font-size:7px;color:#333;padding-left:106px;line-height:36px}
</style>
</head>
<body>

<div class="abs topbar">
  <div class="abs left"><span>🛒 Cart:0 item(s)-$0.00 ⌄</span><span>En ⌄</span><span>$ ⌄</span></div>
  <div class="abs right"><span>My Account</span><span>My Wishlist</span><span>Sign in</span></div>
</div>

<header class="abs header">
  <div class="abs brand"><div class="brand-dot">KLVN</div></div>
  <nav class="abs nav">
    <span style="left:0">ABOUT US</span>
    <span style="left:56px">FAQS</span>
    <span style="left:92px">PRODUCTS</span>
    <span style="left:157px">POLICIES</span>
    <span style="left:210px">TERMS &amp; CONDITIONS</span>
    <span style="left:319px">CONTACT US</span>
    <span style="left:395px">BLOG</span>
  </nav>
  <div class="abs nav-dot"></div>
</header>

<section class="abs hero" role="img" aria-label="Photo of children's hands stacked together in a circle">
  <div class="abs hero-text">For every bar purchased,<br>KLVN will donate a bar to save a child's life.<br>Buy a bar, give a bar.</div>
  <div class="abs hero-dots"><i></i><i></i><i></i></div>
</section>

<section class="abs approach">
  <div class="abs tag" style="left:102px;top:14px;width:106px">OUR APPROACH</div>
  <p class="abs intro" style="left:103px;top:42px">Living a healthy life is needlessly complicated.<br>We're here to change that.</p>
  <div class="abs video" role="img" aria-label="Video still of the founder speaking">
    <div class="abs video-title"><b><i></i></b>About KLVN - Founder &amp; CEO</div>
    <div class="abs video-icons">
      <div><svg width="9" height="8" viewBox="0 0 10 9"><path d="M5 9 1 5a2.3 2.3 0 0 1 4-3 2.3 2.3 0 0 1 4 3z" fill="#fff"/></svg></div>
      <div><svg width="9" height="9" viewBox="0 0 10 10"><circle cx="5" cy="5" r="4" fill="none" stroke="#fff"/><path d="M5 2.5V5l2 1" stroke="#fff" fill="none"/></svg></div>
      <div><svg width="9" height="9" viewBox="0 0 10 10"><path d="M1 5 9 1 6 9 5 6z" fill="#fff"/></svg></div>
    </div>
    <div class="abs video-bar">
      <svg class="abs" style="left:24px;top:6px" width="8" height="8" viewBox="0 0 8 8"><path d="M1 0 7 4 1 8z" fill="#bbb"/></svg>
      <span class="abs" style="left:63px">0:00/ 1:37</span>
      <span class="abs" style="right:12px;font-weight:700;color:#eee">Vidreel</span>
    </div>
  </div>
  <div class="abs" style="left:385px;top:12px;width:1px;height:200px;background:#5a5348"></div>
  <p class="abs label" style="left:409px;top:12px">BUY A SERUM<br>KLVN SOAP</p>
  <div class="abs photo" style="left:410px;top:60px;width:60px;height:100px;background:linear-gradient(160deg,#f39a94,#e06a66);border-radius:10px" role="img" aria-label="Pink bar of soap"></div>
  <div class="abs tag" style="left:420px;top:197px;width:56px;height:17px;line-height:17px;font-size:6px;font-weight:600">SHOP NOW</div>
  <p class="abs label" style="left:515px;top:13px">WORLD GIFTS<br>FOR BABIES</p>
  <div class="abs photo" style="left:516px;top:51px;width:146px;height:73px;background:linear-gradient(120deg,#d9c2a8,#a9876a)" role="img" aria-label="Photo of a father washing hands with his baby"></div>
  <div class="abs photo" style="left:516px;top:139px;width:146px;height:72px;background:linear-gradient(120deg,#7b7f84,#dcdfe2)" role="img" aria-label="Photo of soapy hands under a tap"></div>
</section>

<section class="abs latest">
  <div class="abs tag" style="left:102px;top:16px;width:106px">LATEST PRODUCTS</div>
  <div class="abs arrow" style="left:101px">❮</div>
  <div class="abs arrow" style="left:653px">❯</div>
  <div class="abs photo" style="left:129px;top:57px;width:120px;height:84px;background:linear-gradient(160deg,#5b8f3a,#e9e5dc 50%,#d9b98a)" role="img" aria-label="Product photo of a soap bar with a blue flower"></div>
  <div class="abs photo" style="left:258px;top:57px;width:120px;height:84px;background:linear-gradient(160deg,#f6f1e4,#ddd2a8 55%,#4f8a2c)" role="img" aria-label="Product photo of stacked natural soap bars with limes"></div>
  <div class="abs photo" style="left:388px;top:57px;width:119px;height:84px;background:linear-gradient(160deg,#f3e7d6,#e0b89a 55%,#b08a5c)" role="img" aria-label="Product photo of spa towels, orchids and oil"></div>
  <div class="abs photo" style="left:518px;top:57px;width:120px;height:84px;background:linear-gradient(160deg,#5b8f3a,#e9e5dc 50%,#d9b98a)" role="img" aria-label="Product photo of a soap bar with a blue flower"></div>
</section>

<section class="abs mission">
  <div class="abs tag" style="left:103px;top:17px;width:105px">OUR MISSION</div>
  <p class="abs body-copy" style="left:103px;top:51px;width:170px">Lorem Ipsum has been the industry's standard dummy text ever since the 1500s, when an unknown printer took.</p>
  <div class="abs photo" style="left:103px;top:90px;width:165px;height:70px;background:linear-gradient(120deg,#c9342c,#e8b48c 50%,#b8282a)" role="img" aria-label="Photo of a group of smiling children"></div>
  <div class="abs btn-dark" style="left:103px;top:172px">READ MORE</div>
  <div class="abs offer"><h3>EXTRA 25% OFF</h3><p>ON EVERY ITEMS OVER $500</p></div>
  <div class="abs ship"><h3>FREE SHIPPING</h3><p>Suspendisse ultricies est mi blandit, euismod vestibulum purus.</p></div>
  <div class="abs social-box">
    <h3>FOLLOW US ON FOLKPAGE</h3>
    <div class="page-row"><div class="dot"></div><div><div class="page-name">KLVN SHOP</div><span class="like">Like</span></div></div>
    <p class="small" style="margin-top:4px">43,430 people like KLVN Shop</p>
    <div style="width:149px;height:58px;margin-top:5px;background:linear-gradient(120deg,#8b7d6e,#c07a4a 40%,#4e5a6a 70%,#9a8a80)" role="img" aria-label="Grid of follower profile pictures"></div>
    <p class="small" style="margin-top:6px;padding-left:10px">Folkpage social plugin</p>
  </div>
</section>

<footer class="abs footer">
  <h4 style="left:102px">INFORMATION</h4>
  <div class="links" style="left:102px">Specials<br>New products<br>Best sellers<br>Our stores<br>Contact us<br>Pages configuration<br>Sitemap</div>
  <div class="vline" style="left:214px"></div>
  <h4 style="left:269px">MY ACCOUNT</h4>
  <div class="links" style="left:268px">My orders<br>My merchandise returns<br>My credit slips<br>My addresses<br>My personal info<br>My vouchers</div>
  <div class="vline" style="left:378px"></div>
  <h4 style="left:408px">FOLLOW US</h4>
  <div class="soc" style="top:50px" aria-label="Social link"></div>
  <div class="soc" style="top:72px" aria-label="Social link"></div>
  <div class="soc" style="top:95px" aria-label="Social link"></div>
  <div class="soc" style="top:117px" aria-label="Social link"></div>
  <div class="vline" style="left:504px"></div>
  <h4 style="left:528px">STORE INFORMATION</h4>
  <div class="store">4410 - 4418 Harrow Lane, Brookfield,<br>BF12 7QE<br><b>M -</b>1 (800) 555 0142<br><b>E -</b>hello@klvnmail.com<br><b>F -</b>1 (800) 555 0142</div>
</footer>

<div class="abs copyright">Copyright © 2014 KLVN lantern kept foundation. All rights are reserved.</div>

</body>
</html>
```